K & D A/C Compressors' Business Card

Hello,

I need someone to create a new business card for my business. The name of my Business is: K & D A/C Compressors. I sell automotive air conditioning parts (a/c parts). I would like the business card to incorporate my logo, and to have an automotive feel to it. It is important that the business card feel like it is coming from an automotive parts business.

I already have a logo, which I will provide.

Thanks.
Updates

Project Deadline Extended Reason: I feel like extending the deadline until October 9, 2017, will allow for more time to design the business card. Thank you for your understanding. Added Monday, October 2, 2017

Target Market(s)

Consumers who need automotive a/c parts, and auto mechanics.

Industry/Entity Type

Automotive

Contact Information for Business Card

Business name: K & D A/C Compressors
Business Address: 48207 Southwest 36th Street, North Miami Beach, Florida 33162
Telephone: 305-472-1390
Fax: To be provided once I choose your design.
Website: www.kdcoolunits.example
Email: support@kdcoolunits.example
Names: To be provided once I choose your design.

Font styles to use
Sans Serif

Colors

Designer to choose colors to be used in the design.

Requirements
Must have
• The business card must include all of the "Business Card Details" and the logo I have uploaded.

```html
<!DOCTYPE html>
<html lang="en">
<head>
<meta charset="utf-8">
<title>K &amp; D A/C Compressors – Business Card</title>
<link rel="stylesheet" href="https://fonts.googleapis.com/css2?family=Lato:wght@400;700&display=swap">
<style>
  :root {
    --backdrop: #2a2a2a;
    --brand-blue: #0a9ee0;
    --card-white: #ffffff;
    --logo-grey: #a9a9a9;
    --ink: #1a1a1a;
  }
  * { box-sizing: border-box; margin: 0; padding: 0; }
  html, body {
    width: 1200px;
    height: 900px;
    overflow: hidden;
    background: var(--backdrop);
    font-family: "Lato", sans-serif;
  }
  .canvas {
    position: relative;
    width: 1200px;
    height: 900px;
  }
  .card {
    position: absolute;
    left: 250px;
    width: 700px;
    height: 400px;
    overflow: hidden;
  }

  /* Front */
  .card--front {
    top: 25px;
    background: var(--brand-blue);
    color: var(--card-white);
  }
  .front-logo {
    position: absolute;
    top: 125px;
    left: 0;
    right: 0;
    display: flex;
    align-items: center;
    justify-content: center;
    gap: 18px;
  }
  .logo-mark {
    width: 22px;
    height: 22px;
    border-radius: 50%;
    background: currentColor;
    flex: none;
  }
  .logo-name {
    font-weight: 400;
    font-size: 48px;
    letter-spacing: 1px;
    line-height: 1.1;
    white-space: nowrap;
  }
  .front-web {
    position: absolute;
    bottom: 48px;
    left: 0;
    right: 0;
    text-align: center;
    font-size: 17px;
    letter-spacing: 2px;
  }

  /* Back */
  .card--back {
    top: 475px;
    background: var(--card-white);
    color: var(--ink);
  }
  .back-logo {
    position: absolute;
    top: 150px;
    left: 28px;
    color: var(--logo-grey);
    display: flex;
    align-items: center;
    gap: 10px;
  }
  .back-logo .logo-mark { width: 14px; height: 14px; }
  .back-logo .logo-name { font-size: 27px; letter-spacing: 0.5px; line-height: 1.2; }
  .divider {
    position: absolute;
    left: 360px;
    top: 92px;
    width: 2px;
    height: 188px;
    background: var(--brand-blue);
  }
  .contact {
    position: absolute;
    left: 385px;
    top: 92px;
  }
  .contact-name {
    color: var(--brand-blue);
    font-weight: 700;
    font-size: 31px;
    line-height: 1.1;
  }
  .contact-role {
    font-size: 19px;
    margin-bottom: 14px;
  }
  .contact-list { list-style: none; }
  .contact-list li {
    display: flex;
    align-items: center;
    gap: 14px;
    font-size: 18px;
    line-height: 28px;
    white-space: nowrap;
  }
  .contact-list svg {
    width: 18px;
    height: 18px;
    flex: none;
    fill: var(--brand-blue);
  }
  .address {
    position: absolute;
    left: 40px;
    bottom: 40px;
    font-size: 21px;
    white-space: nowrap;
  }
  .bottom-band {
    position: absolute;
    left: 0;
    right: 0;
    bottom: 0;
    height: 12px;
    background: var(--brand-blue);
  }
</style>
</head>
<body>
<main class="canvas">

  <section class="card card--front" aria-label="Card front">
    <div class="front-logo">
      <span class="logo-mark"></span>
      <span class="logo-name">K &amp; D A/C Compressors</span>
    </div>
    <p class="front-web">www.kdcoolunits.example</p>
  </section>

  <section class="card card--back" aria-label="Card back">
    <div class="back-logo">
      <span class="logo-mark"></span>
      <span class="logo-name">K &amp; D A/C Compressors</span>
    </div>
    <div class="divider"></div>
    <div class="contact">
      <p class="contact-name">Corin Vaskell</p>
      <p class="contact-role">Manager</p>
      <ul class="contact-list">
        <li>
          <svg viewBox="0 0 24 24" aria-hidden="true"><path d="M6.6 10.8c1.4 2.8 3.8 5.1 6.6 6.6l2.2-2.2c.3-.3.7-.4 1-.2 1.1.4 2.300.6 3.6.6.6 0 1 .4 1 1V20c0 .6-.4 1-1 1C10.6 21 3 13.4 3 4c0-.6.4-1 1-1h3.5c.6 0 1 .4 1 1 0 1.3.2 2.5.6 3.6.1.3 0 .7-.2 1z"/></svg>
          305-472-1390
        </li>
        <li>
          <svg viewBox="0 0 24 24" aria-hidden="true"><path d="M6 2h12v5H6zM4 8h16a2 2 0 0 1 2 2v6h-4v6H6v-6H2v-6a2 2 0 0 1 2-2zm4 8v4h8v-4z"/></svg>
          305-472-1391
        </li>
        <li>
          <svg viewBox="0 0 24 24" aria-hidden="true"><path d="M2 5h20v14H2zm2 2v.5l8 5 8-5V7zm0 2.8V17h16V9.8l-8 5z"/></svg>
          support@kdcoolunits.example
        </li>
        <li>
          <svg viewBox="0 0 24 24" aria-hidden="true"><path d="M12 2a10 10 0 1 0 0 20 10 10 0 0 0 0-20zm6.9 9h-3a15 15 0 0 0-1.3-6A8 8 0 0 1 18.9 11zM12 4.1c.9 1.3 1.7 3.6 1.9 6.9h-3.8c.2-3.3 1-5.6 1.9-6.9zM9.4 5a15 15 0 0 0-1.3 6h-3A8 8 0 0 1 9.4 5zM5.1 13h3a15 15 0 0 0 1.3 6A8 8 0 0 1 5.1 13zm6.9 6.9c-.9-1.3-1.700-3.6-1.9-6.9h3.8c-.2 3.3-1 5.6-1.9 6.9zm2.6-.9a15 15 0 0 0 1.3-6h3a8 8 0 0 1-4.3 6z"/></svg>
          www.kdcoolunits.example
        </li>
      </ul>
    </div>
    <p class="address">48207 Southwest 36th Street, Palmetto Shores, Florida 34990</p>
    <div class="bottom-band"></div>
  </section>

</main>
</body>
</html>
```